Post Card Design - Photo on front, details on back. Logo on both sides.

Back: See the photo of my old card. The back worked well, as it gave me lots of space to write on. The address details are still correct, but the logo has changed to Josephine Sans. Logo can be on one line or on two (if two, align it on the left).
Don't include the 'BEAUTIFUL WEDDING DRESSES...' bit.
I'd like to print this on thicker, slightly coarse paper, so don't go too small on detail.
Here are the Quorl paper details: Paper Stock: Natural Uncoated
Paper Thickness: Premium
Finish: None
Front of Card: I'd like to see options for both pictures:
I think the painted image would look best with a frame in a pale shade and the logo in the frame fairly subtle.
The actual dress photo I'd like to see cropped a bit like in my mock up. You'll need to have a look at how the logo would be best placed on this. You can place it anywhere, or add a banner.
See my website for my brand's look: lorabetwick.co.nz
Target Market(s)
Brides
Industry/Entity Type
Wedding Dresses
Contact Information for Business Card
Front: Photo and logo. Back: with details and lots of empty space. See attached photos for loose brief.
Other font styles liked:
- Josephine Sans
Requirements
Must have
- I hand-write the gown designs and price on the back of the card, so there needs to be plenty of empty space.
Nice to have
- As per brief.
Should not have
- It must look clean, romantic, modern. Timeless.

```html
<!DOCTYPE html>
<html lang="en">
<head>
<meta charset="utf-8">
<title>Lora Betwick – Postcard</title>
<link rel="stylesheet" href="https://fonts.googleapis.com/css2?family=Josefin+Sans:wght@300;400;700&display=swap">
<style>
  :root {
    --canvas: #ffffff;
    --cream: #f3e3bf;
    --peach: #f2b89c;
    --rose: #e98c98;
    --blush: #f7d3cf;
    --frame: #ffffff;
    --back-paper: #fbf8f1;
    --back-tint: #f6e9e6;
    --logo-grey: #b9b9b9;
    --line-grey: #c8c8c8;
    --detail-grey: #9d9d9d;
    --phone-grey: #a9a9a9;
  }
  * { margin: 0; padding: 0; box-sizing: border-box; }
  html, body {
    width: 1200px;
    height: 1200px;
    overflow: hidden;
    background: var(--canvas);
    font-family: "Josefin Sans", sans-serif;
  }
  .canvas { position: relative; width: 1200px; height: 1200px; }

  .card {
    position: absolute;
    top: 262px;
    width: 400px;
    height: 679px;
    overflow: hidden;
  }

  /* Front */
  .card-front { left: 197px; }
  .front-artwork {
    position: absolute;
    inset: 0;
    background:
      radial-gradient(circle at 30% 80%, var(--rose) 0%, rgba(233,140,152,0) 45%),
      radial-gradient(circle at 85% 35%, var(--peach) 0%, rgba(242,184,156,0) 40%),
      radial-gradient(circle at 60% 55%, #f6ecd8 0%, rgba(246,236,216,0) 45%),
      linear-gradient(180deg, var(--cream) 0%, var(--blush) 60%, var(--peach) 100%);
  }
  .front-frame {
    position: absolute;
    inset: 11px;
    border: 2.5px solid var(--frame);
  }
  .front-logo {
    position: absolute;
    left: 48px;
    top: 668px;
    top: 406px;
    color: var(--frame);
    font-weight: 400;
    font-size: 24px;
    line-height: 1.05;
    letter-spacing: 2px;
  }

  /* Back */
  .card-back { left: 647px; background: var(--back-paper); }
  .back-artwork {
    position: absolute;
    inset: 0;
    background:
      radial-gradient(ellipse at 35% 30%, rgba(200,190,185,0.35) 0%, rgba(200,190,185,0) 40%),
      radial-gradient(ellipse at 40% 70%, rgba(240,200,205,0.45) 0%, rgba(240,200,205,0) 55%),
      linear-gradient(180deg, var(--back-paper) 0%, var(--back-tint) 60%, var(--back-paper) 100%);
  }
  .back-logo {
    position: absolute;
    left: 242px;
    top: 24px;
    color: var(--logo-grey);
    font-weight: 400;
    font-size: 24px;
    line-height: 1.05;
    letter-spacing: 2px;
  }
  .writing-lines {
    position: absolute;
    left: 22px;
    top: 217px;
    width: 336px;
    list-style: none;
  }
  .writing-lines li {
    height: 61.3px;
    border-bottom: 1.5px solid var(--line-grey);
  }
  .writing-lines li:first-child { height: 1.5px; }
  .contact {
    position: absolute;
    left: 0;
    right: 0;
    top: 585px;
    text-align: center;
    transform: translateX(-15px);
  }
  .contact-web {
    color: var(--detail-grey);
    font-size: 19px;
    font-weight: 400;
    letter-spacing: 1.5px;
  }
  .contact-phone {
    margin-top: 16px;
    color: var(--phone-grey);
    font-size: 25px;
    font-weight: 700;
    letter-spacing: 1px;
  }
</style>
</head>
<body>
<main class="canvas">
  <section class="card card-front">
    <div class="front-artwork" role="img" aria-label="Vintage painted illustration of a couple embracing among large pink and peach peonies"></div>
    <div class="front-frame"></div>
    <div class="front-logo">LORA<br>BETWICK</div>
  </section>

  <section class="card card-back">
    <div class="back-artwork" role="img" aria-label="Faded, pale version of the painted couple and peony illustration"></div>
    <div class="back-logo">LORA<br>BETWICK</div>
    <ul class="writing-lines">
      <li></li><li></li><li></li><li></li><li></li><li></li>
    </ul>
    <div class="contact">
      <p class="contact-web">lorabetwick.co.nz</p>
      <p class="contact-phone">XXX-XXX-XX</p>
    </div>
  </section>
</main>
</body>
</html>
```